design for a business card that uses our logo for an urgent care center
open to suggestions for slogans, we have included some in the logo contest ie Close to Home - Far
design for a business card that uses our logo for an urgent care center - Emergency Services
Creative Brief
Professional
Norvel Pasko RN, BSN
Practice Administrator
4817 Hwy 29 Oakland, TN 38071
NQP41738@mailbrook.test
open to slogans a few ideas Close to Home. Far from Ordinary We’re Right Where You Need Us. The right choice is right here. Also we need one for my wife Gwen L. Pasko MSN, APRN, NP-C Nurse Practitioner
Something that would allow for notes from my wife to her patients ie, followup apt times, etc pharmacy phone

```html
<!DOCTYPE html>
<html lang="en">
<head>
<meta charset="utf-8">
<title>Harbor Point Urgent Care – Business Card</title>
<link rel="stylesheet" href="https://fonts.googleapis.com/css2?family=Open+Sans:wght@400;600;700&display=swap">
<style>
  :root {
    --backdrop: #2b2b2d;
    --card-white: #ffffff;
    --card-shade: #e9e9ea;
    --brand-red: #c8141e;
    --brand-red-dark: #8e0d13;
    --ink: #2a2a2a;
    --ink-soft: #444444;
    --tab-dark: #2e2e30;
  }
  * { margin: 0; padding: 0; box-sizing: border-box; }
  html, body {
    width: 1200px; height: 816px; overflow: hidden;
    background: var(--backdrop);
    font-family: "Open Sans", Arial, sans-serif;
  }
  .card {
    position: absolute; left: 100px; top: 118px;
    width: 1000px; height: 580px;
    border-radius: 36px; overflow: hidden;
    background: linear-gradient(160deg, var(--card-white) 0%, var(--card-white) 55%, var(--card-shade) 100%);
  }
  .card-band { position: absolute; left: 0; top: 0; width: 1000px; height: 580px; }
  .holder { position: absolute; left: 70px; top: 250px; color: var(--ink); }
  .holder-name { font-size: 27px; font-weight: 700; letter-spacing: 0.5px; text-transform: uppercase; }
  .holder-credentials { font-size: 20px; font-weight: 600; letter-spacing: 0; }
  .holder-title { font-size: 20px; font-weight: 400; color: var(--ink-soft); margin-top: 2px; }
  .contact { position: absolute; left: 70px; top: 352px; list-style: none; color: var(--ink); font-size: 17px; }
  .contact li { display: flex; align-items: flex-start; gap: 10px; line-height: 26px; }
  .contact .address { font-weight: 700; width: 250px; }
  .contact svg { flex: none; margin-top: 5px; }
  .brand { position: absolute; left: 540px; top: 150px; display: flex; align-items: center; gap: 18px; }
  .brand-dot { width: 58px; height: 58px; border-radius: 50%; background: var(--brand-red); flex: none; }
  .brand-name {
    font-size: 34px; font-weight: 600; color: var(--brand-red-dark);
    line-height: 40px; text-transform: uppercase; letter-spacing: 1px;
  }
  .website {
    position: absolute; left: 540px; top: 388px;
    width: 460px; height: 60px; border-radius: 30px 0 0 30px;
    background: var(--tab-dark); color: #ffffff;
    font-size: 24px; display: flex; align-items: center; padding-left: 34px;
  }
</style>
</head>
<body>
  <main class="card">
    <svg class="card-band" viewBox="0 0 1000 580" aria-hidden="true">
      <defs>
        <linearGradient id="band-red" x1="0" y1="0" x2="0" y2="1">
          <stop offset="0" stop-color="#e3212b"/>
          <stop offset="1" stop-color="#9c0f16"/>
        </linearGradient>
      </defs>
      <path d="M0 500 L520 500 C560 500 570 440 620 440 L1000 440 L1000 580 L0 580 Z" fill="url(#band-red)"/>
    </svg>

    <section class="holder">
      <h1 class="holder-name">Norvel Pasko<span class="holder-credentials">, RN, BSN</span></h1>
      <p class="holder-title">Practice Administrator</p>
    </section>

    <ul class="contact">
      <li>
        <svg width="14" height="18" viewBox="0 0 14 18"><path d="M7 0a7 7 0 0 0-7 7c0 5 7 11 7 11s7-6 7-11a7 7 0 0 0-7-7zm0 10a3 3 0 1 1 0-6 3 3 0 0 1 0 6z" fill="#2a2a2a"/></svg>
        <span class="address">4817 Hwy 29 Oakland, TN 38071</span>
      </li>
      <li>
        <svg width="16" height="14" viewBox="0 0 16 14"><path d="M1 3c0-2 3-3 7-3s7 1 7 3v2h-4V3H5v2H1zM3 6h10l2 8H1z" fill="#2a2a2a"/></svg>
        <span>012 555 0148</span>
      </li>
      <li>
        <svg width="16" height="14" viewBox="0 0 16 14"><rect x="1" y="4" width="14" height="8" fill="#2a2a2a"/><rect x="4" y="0" width="8" height="5" fill="#2a2a2a"/></svg>
        <span>012 555 0148</span>
      </li>
      <li>
        <svg width="16" height="12" viewBox="0 0 16 12"><rect width="16" height="12" fill="#2a2a2a"/><path d="M0 0l8 6 8-6" stroke="#fff" stroke-width="1.5" fill="none"/></svg>
        <span>NQP41738@mailbrook.test</span>
      </li>
    </ul>

    <div class="brand">
      <span class="brand-dot" aria-hidden="true"></span>
      <p class="brand-name">Harbor Point<br>Urgent Care</p>
    </div>

    <p class="website">www.harborpointcare.test</p>
  </main>
</body>
</html>
```